EPIC, awesome, creative business card needed - get involved!

I'm launching a boutique, exclusive Property Management real estate agency in Sydney early next year.
The name of the agency will be called "Silver Oak Lane" - it's a play on "follow the yellow brick road" to wealth. The Silver Oak Lane signifies wealth through property investment.
My business will offer management of investment properties (ie Property Management).
The difference with Silver Oak Lane and other agencies is the business will be run by one of Australia's leading property investment experts, and also one of Australia's leading property managers.
It will be exclusively for high net worth properties and individuals, so the business card needs to be extremely sharp, slick and relatively simple.
The information I want on the card is as follows
Marcus Fenwick - Director
M: 0471 926 154
P: 9637 0518
E: marcus@silveroaklane.net.au
W: silveroaklane.net.au
I'm happy with the red from the logo, black - no yellows or funky colors. I want this to be a super corporate and slick business card to match the high end nature of the business.
Good luck everyone, and please ask questions for clarification.

```html
<!DOCTYPE html>
<html lang="en">
<head>
<meta charset="utf-8">
<title>Silver Oak Lane — Business Card</title>
<link href="https://fonts.googleapis.com/css2?family=Oswald:wght@300;400;700&display=swap" rel="stylesheet">
<style>
  :root {
    --card-red: #ad0000;
    --card-red-deep: #9c0000;
    --ink-white: #f4f1ef;
    --backdrop: #e9e7e4;
  }
  * { margin: 0; padding: 0; box-sizing: border-box; }
  html, body {
    width: 1200px;
    height: 900px;
    overflow: hidden;
    background: var(--backdrop);
    font-family: "Oswald", "Arial Narrow", sans-serif;
  }
  .stage { position: relative; width: 1200px; height: 900px; }

  .card {
    position: absolute;
    background: var(--card-red);
    color: var(--ink-white);
    box-shadow: 0 2px 6px rgba(0,0,0,0.18);
  }

  /* Back: contact side, portrait */
  .card-back {
    left: 150px; top: 165px;
    width: 330px; height: 570px;
    padding: 58px 46px 0 46px;
  }
  .wordmark {
    font-weight: 700;
    text-transform: uppercase;
    line-height: 0.9;
    letter-spacing: 0.01em;
  }
  .card-back .wordmark { font-size: 40px; margin-bottom: 60px; }
  .details { margin-left: 58px; }
  .person-name {
    font-weight: 400;
    font-size: 27px;
    letter-spacing: 0.06em;
    text-transform: uppercase;
    line-height: 1.1;
  }
  .person-role {
    position: relative;
    font-weight: 300;
    font-size: 15px;
    letter-spacing: 0.55em;
    text-transform: uppercase;
    border-top: 1.5px solid var(--ink-white);
    padding-top: 3px;
    margin-top: 4px;
    width: 180px;
  }
  .contact-list { list-style: none; margin-top: 24px; }
  .contact-list li {
    font-weight: 400;
    font-size: 19px;
    letter-spacing: 0.07em;
    line-height: 1.45;
  }
  .contact-list .label { display: inline-block; width: 28px; }
  .contact-list .email { font-size: 14px; letter-spacing: 0.02em; margin-top: 4px; }
  .contact-list .web { font-size: 19px; letter-spacing: 0.02em; }

  /* Front: brand side, landscape */
  .card-front {
    left: 560px; top: 285px;
    width: 570px; height: 330px;
    border: 4px solid var(--ink-white);
    display: flex; align-items: center; justify-content: center;
  }
  .brick-field {
    position: absolute; inset: 0;
    background: linear-gradient(135deg, var(--card-red) 0%, var(--card-red-deep) 100%);
  }
  .card-front .wordmark {
    position: relative;
    font-size: 46px;
    text-align: left;
  }
</style>
</head>
<body>
<main class="stage">

  <section class="card card-back" aria-label="Business card, contact side">
    <div class="wordmark">Silver<br>Oak<br>Lane</div>
    <div class="details">
      <h1 class="person-name">Marcus Fenwick</h1>
      <p class="person-role">Director</p>
      <ul class="contact-list">
        <li><span class="label">M:</span>0471 926 154</li>
        <li><span class="label">T:</span>9637 0518</li>
        <li class="email">marcus@silveroaklane.net.au</li>
        <li class="web">silveroaklane.net.au</li>
      </ul>
    </div>
  </section>

  <section class="card card-front" aria-label="Business card, brand side">
    <div class="brick-field" role="img" aria-label="Red brick-grid pattern of interlocking rectangles"></div>
    <div class="wordmark">Silver<br>Oak<br>Lane</div>
  </section>

</main>
</body>
</html>
```